SkyVelour IOS App for iPhone / Luxury private aviation / 1 main screen

Hello there !

SkyVelour Ltd is a VIP aircraft operator. You can see our https://social-example.net/skyvelour page or our https://photo-example.net/sky_velour . Our web page http://skyvelour-demo.net says it all, we don't communicate much except for the music industry activities we have.

We have developed a very simple app, 6 screens total, that will give the user a distance and a flight time between any two airports of the world. Enter a departure point (New York or JFK or KJFK...) and a destination (like Los Angeles, LAX or KLAX) and we will give you the flight time depending on the type of private jet you are selecting in the aircraft database of the app.

You might want to see the attached pdf for the flow...Any design idea is welcome.

We want it to be simple, pure, fast, and of course less will be more. We should see a unity between all these screens, same design spirit of course... On the main screen of the app, we are showing:- the company logo- a departure airport- a destination airport- the selected aircraft with access to a mini photo gallery of the said airplane- a flight time shown in hours and minutes- a distance shown in Miles, Nautical Miles or KM according to the pref page selection- an access to a contact screen- an access to a parameters screen (will develop some of it on a later version).

Thanks !!

Mathis

Target Market(s)

Private aircraft travelers and VIP flights brokers

Industry/Entity Type

Aviation

Font styles to use
Sans Serif

Colors
aaaaaa
5c5c5c
1b1b1b
e9e9e9
ffffff

Requirements
Must have
• Our logo
Nice to have
• Elegant design
Should not have
• Complicated stuff

```html
<!DOCTYPE html>
<html lang="en">
<head>
<meta charset="utf-8">
<title>SkyVelour – Main Screen</title>
<link href="https://fonts.googleapis.com/css2?family=Poppins:wght@300;400;500;600;700&display=swap" rel="stylesheet">
<style>
  :root{
    --ink:#1b1b1b;
    --graphite:#5c5c5c;
    --mist:#aaaaaa;
    --cloud:#e9e9e9;
    --white:#ffffff;
    --panel:#f2f1f1;
    --price:#6ad14a;
    --call:#5cc658;
    --sky-top:#e9a27a;
    --sky-mid:#8a5a66;
    --sky-low:#4a3c48;
  }
  *{box-sizing:border-box;margin:0;padding:0}
  html,body{width:1200px;height:1200px;overflow:hidden}
  body{background:#e6e6e6;font-family:"Poppins",sans-serif;color:var(--ink);position:relative}

  .screen{position:absolute;left:330px;top:30px;width:540px;height:1140px;border-radius:56px;overflow:hidden;background:var(--white);box-shadow:0 20px 60px rgba(0,0,0,.15)}

  .app-header{position:absolute;left:0;top:0;width:100%;height:300px;background:var(--ink)}
  .status-bar{position:absolute;right:34px;top:22px;display:flex;gap:8px;align-items:center}
  .menu-button{position:absolute;left:32px;top:150px}
  .brand{position:absolute;left:0;right:0;top:146px;text-align:center;color:var(--white);font-weight:600;font-size:19px;letter-spacing:4px}
  .bell{position:absolute;right:34px;top:70px}

  .hero{position:absolute;left:0;top:260px;width:100%;height:600px;
    background:linear-gradient(165deg,var(--sky-top) 0%,#c07a76 22%,var(--sky-mid) 48%,var(--sky-low) 80%,#3a3038 100%)}

  .route-card{position:absolute;left:30px;right:30px;top:195px;height:230px;background:var(--white);border-radius:22px;box-shadow:0 10px 30px rgba(0,0,0,.12)}
  .route-row{position:absolute;left:28px;right:110px;height:100px;display:flex;align-items:center;gap:26px}
  .route-row.departure{top:8px}
  .route-row.arrival{top:118px}
  .route-divider{position:absolute;left:28px;right:110px;top:114px;height:1px;background:var(--cloud)}
  .route-label{font-size:14px;letter-spacing:2px;color:var(--mist);font-weight:400}
  .route-city{font-size:31px;font-weight:600;color:var(--ink);line-height:1.1}
  .route-code{font-size:20px;color:var(--mist);font-weight:400;margin-left:26px}
  .swap-button{position:absolute;right:26px;top:46px;width:66px;height:66px;border-radius:16px;background:var(--cloud);display:flex;align-items:center;justify-content:center}

  .aircraft{position:absolute;left:28px;top:790px;color:var(--white)}
  .aircraft-seats{font-size:15px;letter-spacing:2.5px;color:rgba(255,255,255,.8);display:flex;gap:10px;align-items:center}
  .aircraft-name{font-size:44px;font-weight:600;line-height:1.2;margin-top:2px}

  .slots{position:absolute;left:28px;right:28px;top:880px;display:flex;gap:14px}
  .slot{flex:1;height:88px;border-radius:12px;background:rgba(255,255,255,.14);padding:12px 16px;color:var(--white)}
  .slot.active{background:rgba(255,255,255,.85);color:var(--graphite)}
  .slot-day{font-size:12px;letter-spacing:1.5px;font-weight:600}
  .slot-time{font-size:36px;font-weight:300;line-height:1.2}
  .pager{position:absolute;left:0;right:0;top:986px;display:flex;justify-content:center;gap:8px;align-items:center}
  .pager span{width:8px;height:8px;border-radius:50%;background:rgba(255,255,255,.5)}
  .pager span.current{width:11px;height:11px;background:var(--white)}

  .booking{position:absolute;left:0;top:860px;width:100%;height:160px;background:#f9f6f6}
  .distance{position:absolute;left:30px;top:26px}
  .distance-label{font-size:15px;letter-spacing:2px;color:var(--mist)}
  .distance-input{margin-top:12px;width:200px;height:92px;background:var(--white);border-radius:14px;font-size:34px;font-weight:600;display:flex;align-items:center;padding-left:28px}
  .book-button{position:absolute;right:26px;top:18px;width:300px;height:128px;background:var(--ink);border-radius:16px;padding:24px 26px;color:var(--white)}
  .book-price{font-size:26px;color:var(--price);font-weight:400}
  .book-label{font-size:36px;font-weight:700;display:flex;align-items:center;gap:20px;line-height:1.2}

  .contact{position:absolute;left:0;top:1020px;width:100%;height:120px;background:var(--panel);padding:18px 30px}
  .contact-label{font-size:15px;letter-spacing:2.5px;color:var(--mist)}
  .contact-links{display:flex;gap:14px;margin-top:12px;align-items:center}
  .social-link{font-size:14px;font-weight:500;color:var(--graphite);text-decoration:none;background:var(--white);border-radius:12px;padding:12px 14px}
  .call-link{width:50px;height:50px;border-radius:12px;background:var(--call);display:flex;align-items:center;justify-content:center}
  .home-indicator{position:absolute;left:170px;bottom:12px;width:200px;height:5px;border-radius:3px;background:var(--mist)}
</style>
</head>
<body>
<main class="screen">
  <header class="app-header">
    <div class="status-bar">
      <svg width="18" height="14" viewBox="0 0 18 14"><path d="M1 5a12 12 0 0 1 16 0M4 8a7.5 7.5 0 0 1 10 0M7 11a3 3 0 0 1 4 0" fill="none" stroke="#fff" stroke-width="1.8" stroke-linecap="round"/></svg>
      <svg width="32" height="14" viewBox="0 0 32 14"><rect x="1" y="1" width="27" height="12" rx="3" fill="none" stroke="#fff" stroke-width="1.3"/><rect x="3" y="3" width="12" height="8" rx="1.5" fill="#fff"/><rect x="29.5" y="5" width="2" height="4" rx="1" fill="#fff"/></svg>
    </div>
    <svg class="menu-button" width="40" height="30" viewBox="0 0 40 30" aria-label="Menu"><g stroke="#fff" stroke-width="2.4" stroke-linecap="round"><line x1="2" y1="3" x2="38" y2="3"/><line x1="2" y1="11" x2="34" y2="11"/><line x1="2" y1="19" x2="38" y2="19"/><line x1="2" y1="27" x2="22" y2="27"/></g></svg>
    <div class="brand">SKYVELOUR</div>
    <svg class="bell" width="34" height="40" viewBox="0 0 34 40" aria-label="Notifications"><path d="M6 30V18a11 11 0 0 1 22 0v12l3 4H3z M13 36a4 4 0 0 0 8 0" fill="none" stroke="#fff" stroke-width="2.2" stroke-linejoin="round"/><circle cx="25" cy="8" r="4" fill="none" stroke="#fff" stroke-width="2"/></svg>
  </header>

  <section class="hero" role="img" aria-label="Photo of a private jet flying over the sea at sunset"></section>

  <section class="route-card">
    <div class="route-row departure">
      <svg width="46" height="40" viewBox="0 0 46 40"><path d="M4 22l36-12c4-1 5 3 1 4L12 26l-6-1z M16 18l-6-8h5l10 5 M20 24l-2 8h4l6-10" fill="none" stroke="#1b1b1b" stroke-width="2" stroke-linejoin="round"/><line x1="6" y1="37" x2="18" y2="37" stroke="#1b1b1b" stroke-width="2"/></svg>
      <div><div class="route-label">DEPARTURE</div><div class="route-city">New York<span class="route-code">NYC</span></div></div>
    </div>
    <div class="route-divider"></div>
    <div class="route-row arrival">
      <svg width="46" height="40" viewBox="0 0 46 40"><path d="M4 14l36 12c4 1 3 5-1 4L8 22l-4-4z M12 16l0-12h5l6 14 M24 24l4 6h4l-2-6" fill="none" stroke="#1b1b1b" stroke-width="2" stroke-linejoin="round"/><line x1="28" y1="37" x2="40" y2="37" stroke="#1b1b1b" stroke-width="2"/></svg>
      <div><div class="route-label">ARRIVAL</div><div class="route-city">Shenzhen<span class="route-code">SZX</span></div></div>
    </div>
    <div class="swap-button" aria-label="Swap airports">
      <svg width="32" height="32" viewBox="0 0 32 32"><path d="M6 14a10 10 0 0 1 18-5M26 18a10 10 0 0 1-18 5" fill="none" stroke="#1b1b1b" stroke-width="2" stroke-linecap="round"/><path d="M24 3v6h-6M8 29v-6h6" fill="none" stroke="#1b1b1b" stroke-width="2" stroke-linecap="round" stroke-linejoin="round"/></svg>
    </div>
  </section>

  <div class="aircraft">
    <div class="aircraft-seats"><svg width="18" height="20" viewBox="0 0 18 20"><circle cx="6" cy="3" r="2.5" fill="#fff"/><path d="M4 7v7h7l3 5M4 14l-2 5" fill="none" stroke="#fff" stroke-width="2" stroke-linecap="round"/></svg>19 SEATS</div>
    <div class="aircraft-name">Aurel 9S</div>
  </div>

  <div class="slots">
    <div class="slot"><div class="slot-day">FRIDAY</div><div class="slot-time">10 am</div></div>
    <div class="slot active"><div class="slot-day">SUNDAY</div><div class="slot-time">07 pm</div></div>
    <div class="slot"><div class="slot-day">MONDAY</div><div class="slot-time">03 pm</div></div>
  </div>
  <div class="pager"><span></span><span></span><span class="current"></span><span></span><span></span></div>

  <section class="booking">
    <div class="distance">
      <div class="distance-label">ENTER KMS</div>
      <div class="distance-input">200</div>
    </div>
    <div class="book-button">
      <div class="book-price">$3.5K</div>
      <div class="book-label">Book Now
        <svg width="40" height="24" viewBox="0 0 40 24"><path d="M2 12h34M26 3l10 9-10 9" fill="none" stroke="#fff" stroke-width="2.4" stroke-linecap="round" stroke-linejoin="round"/></svg>
      </div>
    </div>
  </section>

  <footer class="contact">
    <div class="contact-label">CONNECT WITH US</div>
    <nav class="contact-links">
      <a class="social-link" href="https://photo-example.net/sky_velour">PhotoNet</a>
      <a class="social-link" href="https://social-example.net/skyvelour">SocialNet</a>
      <a class="social-link" href="http://skyvelour-demo.net">ChirpNet</a>
      <span class="call-link" aria-label="Call">
        <svg width="26" height="26" viewBox="0 0 26 26"><path d="M6 2l4 5-2 3c1 3 4 6 7 7l3-2 5 4-3 4C11 23 3 15 2 5z" fill="#fff"/></svg>
      </span>
    </nav>
    <div class="home-indicator"></div>
  </footer>
</main>
</body>
</html>
```